one side yoga classes, other side rental log cabin

I need a flyer to advertise yoga classes on a lake , and to describe the various styles of classes, and who they can benefit, Days Times .prices
Linked to it is a rental log cabin that can be rented privetly to families or Groups (8 max) www.fernvalestays.com This also is rented to yoga teacher that would like to Hire Cabin and the Studio www.velinoshaven.co.uk or
for Holistic weekends.

Teacher

```html
<!DOCTYPE html>
<html lang="en">
<head>
<meta charset="utf-8">
<title>Velinos Haven – Yoga Classes Flyer</title>
<link rel="stylesheet" href="https://fonts.googleapis.com/css2?family=Jost:ital,wght@0,400;0,500;0,600;1,400&display=swap">
<style>
  :root {
    --navy: #1d1f5c;
    --lavender: #dcd8ee;
    --lavender-deep: #b9b2dc;
    --ink-grey: #555760;
    --white: #ffffff;
  }
  * { box-sizing: border-box; margin: 0; padding: 0; }
  html, body { width: 1200px; height: 1000px; overflow: hidden; background: var(--white); }
  body { position: relative; font-family: "Jost", "Futura", sans-serif; }

  .page {
    position: absolute; top: 133px; width: 536px; height: 755px;
    overflow: hidden; background: var(--white);
    box-shadow: 3px 3px 6px rgba(0,0,0,0.3);
  }
  .page--classes { left: 53px; }
  .page--retreat { left: 616px; }

  /* ---------- Classes page ---------- */
  .studio-photo {
    position: absolute; inset: 0;
    background:
      linear-gradient(180deg, rgba(150,185,225,0.9) 0%, rgba(170,195,220,0.8) 35%, rgba(120,130,140,0.6) 55%, rgba(0,0,0,0) 60%),
      linear-gradient(180deg, #7d6a5a 0%, #6b5646 50%, #b0824c 68%, #d9a467 82%, #a7764a 100%);
  }
  .page-title {
    position: absolute; left: 0; right: 0; top: 40px; text-align: center;
    color: var(--navy); font-weight: 400; font-size: 45px; letter-spacing: 5px;
  }
  .schedule {
    position: absolute; left: 29px; top: 131px; width: 480px;
    color: var(--white); font-weight: 500; font-size: 12px; line-height: 16px;
    text-shadow: 0 0 3px rgba(0,0,0,0.6);
  }
  .schedule p { margin-bottom: 13px; }
  .schedule .styles { font-weight: 400; font-style: italic; }
  .charity-note {
    position: absolute; left: 29px; top: 457px; color: var(--white);
    font-style: italic; font-size: 12px; text-shadow: 0 0 3px rgba(0,0,0,0.6);
  }
  .info { position: absolute; left: 29px; width: 380px; color: var(--white);
    font-weight: 500; font-size: 12px; line-height: 17px; text-shadow: 0 0 3px rgba(0,0,0,0.6); }
  .info--events { top: 492px; }
  .info--hire { top: 546px; }

  .ornament { position: absolute; background: rgba(220,216,238,0.7); border-radius: 50% 50% 0 0; }
  .ornament--classes { left: 340px; top: 545px; width: 196px; height: 130px; }
  .ornament--retreat { left: 320px; top: 560px; width: 216px; height: 120px; }

  .footer {
    position: absolute; left: 0; right: 0; bottom: 0; height: 80px;
    background: var(--lavender); border-top: 2px dotted var(--white);
    padding: 20px 0 0 30px;
    color: var(--navy); font-size: 10.5px; line-height: 13.5px;
  }
  .footer span { display: block; }
  .footer .indent-1 { padding-left: 45px; }
  .footer .indent-2 { padding-left: 62px; }

  .contact-circle {
    position: absolute; left: 350px; top: 590px; width: 210px; height: 210px;
    border-radius: 50%; background: var(--white);
    padding: 55px 0 0 12px; color: var(--navy);
  }
  .contact-circle .name { font-size: 18px; display: block; margin-left: 20px; }
  .contact-circle .phone { font-size: 21px; display: block; }

  /* ---------- Retreat page ---------- */
  .lake-photo {
    position: absolute; left: 0; top: 0; width: 536px; height: 347px;
    background: linear-gradient(180deg, #bcd0ea 0%, #d9e4f2 30%, #8a9a5a 38%, #6f7f4a 62%, #8598ae 70%, #6e86a6 100%);
  }
  .page--retreat .page-title { top: 42px; font-size: 43px; letter-spacing: 4px; }
  .offerings {
    position: absolute; left: 0; right: 0; top: 285px;
    display: flex; justify-content: center; gap: 44px;
    color: var(--white); font-size: 25px; letter-spacing: 0.5px;
  }
  .navy-band { position: absolute; left: 0; right: 0; top: 345px; height: 17px; background: var(--navy); }
  .lavender-band { position: absolute; left: 0; right: 0; top: 362px; height: 34px; background: var(--lavender); }
  .intro {
    position: absolute; left: 29px; top: 446px; width: 265px;
    color: var(--ink-grey); font-size: 10.5px; line-height: 14.5px;
  }
  .intro p { margin-bottom: 12px; }
  .gazebo-photo {
    position: absolute; left: 355px; top: 590px; width: 200px; height: 200px; border-radius: 50%;
    border: 5px solid var(--lavender);
    background: linear-gradient(180deg, #6d8aa0 0%, #4f5c55 40%, #7a6a55 70%, #b8a286 100%);
  }
</style>
</head>
<body>

<section class="page page--classes">
  <div class="studio-photo" role="img" aria-label="Woman in a yoga pose on a mat in a sunlit wooden studio overlooking a lake, with a statue by the window"></div>
  <h1 class="page-title">YOGA CLASSES</h1>
  <div class="schedule">
    <p>Class schedule</p>
    <p class="styles">Gentle, Dru, Hatha and Power styles to ease stress and build strength, balance and flexibility.</p>
    <p>Tuesday - 8 am to 9.00 am Gentle Yoga for all - £7 (Velinos Studio)</p>
    <p>Tuesday - 10 am to 11.15am Dru Yoga - £7 (Velinos studio)</p>
    <p>Tuesday - 7.00pm to 8.15pm Hatha/Dru - £9<br>(Brackwell memorial Hall, Brackwell . Norfolk).<br>(Please note:- this class does not run on the first Tuesday of each month).</p>
    <p>Friday - 10am to 11.15 am Hatha Yoga - £7 (Velinos studio)</p>
    <p>Last Sunday of the month 8.30am to 10.00 Power Yoga&nbsp; - £10<br>(Velinos Studio)</p>
  </div>
  <p class="charity-note">A proportion of every class payment is put towards our supported charities</p>
  <p class="info info--events">For our events and retreats schedule please log into our web site<br>www.velinoshaven.co.uk</p>
  <p class="info info--hire">The retreat can be hired by other teachers and group,<br>&nbsp;so please call marla on 07700 900318 for details.</p>
  <div class="ornament ornament--classes" role="img" aria-label="Lavender floral scroll ornament"></div>
  <footer class="footer">
    <span>Velinos Haven, 4 Alder Lakes, Alderby PE00 0AA</span>
    <span class="indent-1">Tel:&nbsp; 01632 960418</span>
    <span class="indent-2">www.velinoshaven.co.uk</span>
  </footer>
  <div class="contact-circle">
    <span class="name">Contact Marla</span>
    <span class="phone">07700 900318</span>
  </div>
</section>

<section class="page page--retreat">
  <div class="lake-photo" role="img" aria-label="Log cabin retreat among trees on the shore of a lake under a blue sky"></div>
  <h1 class="page-title">VELINOS HAVEN</h1>
  <div class="offerings"><span>Yoga</span><span>Meditation</span><span>Relaxation</span></div>
  <div class="navy-band"></div>
  <div class="lavender-band"></div>
  <div class="intro">
    <p>Velinos Haven is located on the shores of Alder Lakes, near Marshford, Norfolk.&nbsp; The retreat enjoys the surroundings of some of the most spectacular views in the UK with a bird and wildfowl sanctuary on our doorstep - perfect to relax and unwind for a few days away.</p>
    <p>Our lakeside log cabin can be rented privately by families or groups (8 max) - www.fernvalestays.com. Teachers may hire the cabin and studio for holistic weekends.</p>
    <p>For more retreat details and the gallery visit our website www.velinoshaven.co.uk</p>
  </div>
  <div class="ornament ornament--retreat" role="img" aria-label="Lavender floral scroll ornament"></div>
  <footer class="footer">
    <span>Velinos Haven, 4 Alder Lakes, Alderby PE00 0AA</span>
    <span class="indent-1">Tel:&nbsp; 01632 960418</span>
    <span class="indent-2">www.velinoshaven.co.uk</span>
  </footer>
  <div class="gazebo-photo" role="img" aria-label="Wooden gazebo with seating beside the lake"></div>
</section>

</body>
</html>
```